Speisekarten-Design für Café
Vielen lieben Dank!
Zielgruppe
Café mit Angebot von Frühstück und Torten/Kuchen (BIO!) und Verkauf von Dekoartikeln. Zielgruppe sind sowohl Familien, als auch ältere Personen, die sich zum Kaffeeklatsch treffen. Ebenso 'Freundinnen' und junge Mütter.
In den Räumlichkeiten war schon seit 24 Jahren ein Café, die Besitzerin ist aber verstorben
Aufgabenstellung
Karte in DIN A 5 Format, da die Tische nicht so groß sind. Die erste Seite soll die 'Geschichte' der Lokalität enthalten. Keine 'bunten' Bilder (Comics) von irgendwelchen Torten und/oder Frühstücken

```html
<!DOCTYPE html>
<html lang="de">
<head>
<meta charset="utf-8">
<title>Kaffeestube Amsel – Speisekarte</title>
<link href="https://fonts.googleapis.com/css2?family=Amatic+SC:wght@400&family=Pompiere&display=swap" rel="stylesheet">
<style>
  :root {
    --board: #2a2c2f;
    --chalk: #ffffff;
    --chalk-soft: rgba(255,255,255,0.18);
    --chalk-faint: rgba(255,255,255,0.06);
    --paper: #ffffff;
    --ink: #2a2c2f;
  }
  html, body {
    margin: 0;
    padding: 0;
    width: 1200px;
    height: 837px;
    overflow: hidden;
    background: var(--paper);
  }
  .spread {
    position: relative;
    width: 1200px;
    height: 837px;
    font-family: "Pompiere", sans-serif;
    color: var(--chalk);
  }
  .page {
    position: absolute;
    top: 11px;
    width: 564px;
    height: 801px;
    background: var(--board);
    overflow: hidden;
  }
  .page--story { left: 27px; }
  .page--menu { left: 620px; width: 567px; }
  .page__frame {
    position: absolute;
    inset: 10px;
    border: 1.5px solid var(--chalk);
    pointer-events: none;
  }

  /* Story page */
  .brand {
    position: absolute;
    top: 150px;
    left: 0;
    right: 0;
    text-align: center;
    font-size: 46px;
    line-height: 1;
  }
  .story__title {
    position: absolute;
    top: 364px;
    left: 0;
    right: 0;
    margin: 0;
    text-align: center;
    font-weight: 400;
    font-size: 42px;
    line-height: 1;
  }
  .story__text {
    position: absolute;
    top: 448px;
    left: 50%;
    width: 356px;
    margin: 0 0 0 -178px;
    text-align: center;
    font-size: 19px;
    line-height: 30px;
  }
  .ornament {
    position: absolute;
    background: linear-gradient(180deg, var(--chalk-soft), var(--chalk-faint));
  }
  .ornament--corner-left { left: 0; top: 695px; width: 62px; height: 96px; border-radius: 0 60% 0 0; }
  .ornament--corner-right { right: 0; top: 695px; width: 62px; height: 96px; border-radius: 60% 0 0 0; }
  .ornament--vine-top { right: 0; top: 0; width: 112px; height: 300px; border-radius: 0 0 0 60px; }
  .ornament--vine-bottom { left: 0; top: 372px; width: 122px; height: 429px; border-radius: 0 60px 0 0; }

  /* Menu page */
  .menu-section {
    position: absolute;
    left: 0;
    width: 554px;
    text-align: center;
  }
  .menu-section--breakfast { top: 52px; }
  .menu-section--coffee { top: 290px; }
  .menu-section--cake { top: 527px; }
  .ribbon {
    position: relative;
    width: 232px;
    height: 36px;
    margin: 0 auto;
  }
  .ribbon svg { position: absolute; inset: 0; }
  .ribbon__label {
    position: relative;
    margin: 0;
    font-family: "Amatic SC", sans-serif;
    font-weight: 400;
    font-size: 26px;
    line-height: 36px;
    letter-spacing: 1px;
    color: var(--ink);
  }
  .menu-list {
    list-style: none;
    margin: 14px 0 0;
    padding: 0;
    font-size: 19px;
    line-height: 40px;
  }
</style>
</head>
<body>
<main class="spread">

  <section class="page page--story">
    <div class="page__frame"></div>
    <div class="brand">Kaffeestube Amsel</div>
    <h1 class="story__title">Kaffeestube Amsel</h1>
    <p class="story__text">Lorem ipsum dolor sit amet, consectetuer adipiscing elit, sed diam nonummy nibh euismod tincidunt ut laoreet dolore magna aliquam erat volutpat. Ut wisi enim ad minim veniam, quis nostrud exerci tation ullamcorper suscipit loLorem ipsum dolor sit amet, consectetuer adipiscing elit, sed diam nonummy nibh euismod tincidunt ut laoreet dolore magna aliquam erat volutpat. Ut wisi enim ad minim veniam, quis nostrud exerci tation ullamcorper suscipit loLorem ipsum dolor sit amet, consectetuer adipiscing elit, sed diam nonummy nibh euismod tincidunt ut laoreet dolore magna aliquam erat volutpat. Ut wisi enim</p>
    <div class="ornament ornament--corner-left" role="img" aria-label="Verschnörkeltes Eckornament in Kreideweiß"></div>
    <div class="ornament ornament--corner-right" role="img" aria-label="Verschnörkeltes Eckornament in Kreideweiß"></div>
  </section>

  <section class="page page--menu">
    <div class="page__frame"></div>
    <div class="ornament ornament--vine-top" role="img" aria-label="Gezeichnete Blätterranke mit Spiralen in Kreideweiß"></div>
    <div class="ornament ornament--vine-bottom" role="img" aria-label="Gezeichnete Blätterranke mit Spiralen in Kreideweiß"></div>

    <div class="menu-section menu-section--breakfast">
      <div class="ribbon">
        <svg viewBox="0 0 232 36" width="232" height="36" aria-hidden="true"><path d="M0 2 Q116 12 232 2 L216 18 L232 34 Q116 26 0 34 L16 18 Z" fill="#ffffff"/></svg>
        <h2 class="ribbon__label">Frühstück</h2>
      </div>
      <ul class="menu-list">
        <li>Lorem ipsum dolor sit amet,</li>
        <li>Lorem ipsum dolor sit amet,</li>
        <li>Lorem ipsum dolor sit amet,</li>
      </ul>
    </div>

    <div class="menu-section menu-section--coffee">
      <div class="ribbon">
        <svg viewBox="0 0 232 36" width="232" height="36" aria-hidden="true"><path d="M0 2 Q116 12 232 2 L216 18 L232 34 Q116 26 0 34 L16 18 Z" fill="#ffffff"/></svg>
        <h2 class="ribbon__label">Kaffee</h2>
      </div>
      <ul class="menu-list">
        <li>Lorem ipsum dolor sit amet,</li>
        <li>Lorem ipsum dolor sit amet,</li>
        <li>Lorem ipsum dolor sit amet,</li>
      </ul>
    </div>

    <div class="menu-section menu-section--cake">
      <div class="ribbon">
        <svg viewBox="0 0 232 36" width="232" height="36" aria-hidden="true"><path d="M0 2 Q116 12 232 2 L216 18 L232 34 Q116 26 0 34 L16 18 Z" fill="#ffffff"/></svg>
        <h2 class="ribbon__label">Kuchen</h2>
      </div>
      <ul class="menu-list">
        <li>Lorem ipsum dolor sit amet,</li>
        <li>Lorem ipsum dolor sit amet,</li>
        <li>Lorem ipsum dolor sit amet,</li>
      </ul>
    </div>
  </section>

</main>
</body>
</html>
```